Our Pantry Remedy

I am a pharmacist turn chef and my current website www.ourpantryremedy-demo.com is in desperate need of a make over. I want to be able to add how to videos, photographs and have tabs. The tabs needed will be Home, About, Recipes, Health & Wellness, Services, Confidentiality, Affordability, Blog, Articles and Friday Cocktails. Eventually I will want a news letter, but do not want that now, only the ability to add it later. I will also want to add a market place tab later to sell merchandise and ebooks. The ability to navigate should be easy and not confusing and the ability to post should be easy. I will need social media Friendlyn, Clipboardia, searcho plus, searcho, Snapvue and chirpit. In addition I will need some direction on how to operate the site. Examples of website I like (but do not want to copy) are www.buildbrightvigor-demo.net www.drpaulvenmore-demo.com. It is best for me to work with someone who can explain things simply.
Updates

Another website I think is nice is www.zbgalley-demo.com  Thanks!

Target Market(s)

The business will be diving right into the delicious side of Key West’s good health as a personal chef, a culinary wellness coach, a wellness cooking teacher, a healthful caterer and a wellness host and entertainer.
The site needs to promote health with the art of food because I am convinced that health is best enhanced, maintained and recovered through nutritious eating and cuisine, and not through pills.
I will be infusing fresh recipes with a Key West flair in hopes to share my passion and insights into nutrition and health with residents and visitors alike. I want everyone to feel welcome to come in and join the fun.

Industry/Entity Type

Chef

Colors

Designer to choose colors to be used in the design.

Requirements
Must have
• Easy navigation, easy operation and posting and social media tools. Spam filters to keep the creeps away and important plugins that make it all work.
Nice to have
• Everything is nice to have

```html
<!DOCTYPE html>
<html lang="en">
<head>
<meta charset="utf-8">
<title>Our Pantry Remedy</title>
<link href="https://fonts.googleapis.com/css2?family=Yanone+Kaffeesatz:wght@400;500&family=Arimo:wght@400&family=Great+Vibes&display=swap" rel="stylesheet">
<style>
:root{
  --page:#ebebeb;
  --panel:#ffffff;
  --ink:#2f2f2f;
  --muted:#6f6f6f;
  --accent:#4f7390;
  --link:#8a6a3c;
  --rule:#e2e2e2;
  --caption-bg:rgba(20,20,20,.78);
  --brand-green:#2f7a4b;
}
*{margin:0;padding:0;box-sizing:border-box}
html,body{width:1200px;height:2487px;overflow:hidden;background:var(--page)}
body{position:relative;font-family:"Arimo",Arial,sans-serif;color:var(--ink)}
.heading{font-family:"Yanone Kaffeesatz","Arial Narrow",sans-serif;font-weight:400;color:var(--ink)}

.brand{position:absolute;left:34px;top:22px;font-family:"Yanone Kaffeesatz",sans-serif;font-size:34px;color:var(--brand-green);line-height:1}
.brand small{display:block;font-size:20px}
.site-title{position:absolute;left:0;right:0;top:26px;text-align:center;font-family:"Yanone Kaffeesatz",sans-serif;font-size:46px;color:#333}
.tagline{position:absolute;left:0;right:0;top:88px;text-align:center;font-size:17px;color:var(--muted)}

.main-nav{position:absolute;left:21px;top:133px;width:1158px;height:68px;background:var(--panel);display:flex;justify-content:center;align-items:center;gap:46px;list-style:none}
.main-nav li{font-family:"Yanone Kaffeesatz",sans-serif;font-size:17px;text-transform:uppercase;letter-spacing:.5px;color:#444}

.hero{position:absolute;left:21px;top:215px;width:1158px;height:452px;background:var(--panel)}
.hero-photo{position:absolute;left:0;top:0;width:1158px;height:417px;background:linear-gradient(160deg,#f3eee9 0%,#e6d6c8 35%,#8aa65a 55%,#c07a3a 75%,#6b5a4a 100%)}
.hero-caption{position:absolute;right:0;top:218px;width:440px;height:199px;background:var(--caption-bg);color:#fff;text-align:right;padding:30px 18px 0 18px}
.hero-caption h2{font-family:"Yanone Kaffeesatz",sans-serif;font-weight:400;font-size:28px;margin-bottom:14px}
.hero-caption p{font-size:14px;line-height:1.45}
.pager{position:absolute;right:10px;bottom:6px;display:flex;gap:0}
.pager span{width:30px;height:26px;font-size:15px;color:#999;display:flex;align-items:center;justify-content:center;border-right:1px solid var(--rule)}
.pager span.active{color:#c0392b}

.intro{position:absolute;left:21px;top:771px;width:1158px;height:217px;background:var(--panel);display:flex}
.intro-col{flex:1;padding:22px 14px 0;text-align:center;border-right:2px solid var(--rule)}
.intro-col:last-child{border-right:none}
.intro-col h3{font-size:24px;margin-bottom:18px}
.intro-col p{font-size:13.5px;line-height:1.45;color:var(--accent)}
.intro-col p.plain{color:var(--muted)}

.post-card{position:absolute;width:366px;height:395px;background:var(--panel);padding:26px 19px 0}
.post-card h3{font-size:27px;line-height:1.1;margin-bottom:14px;min-height:30px}
.post-card p{font-size:14px;line-height:1.45;color:var(--muted);height:50px}
.post-card p.tinted{color:var(--accent)}
.post-photo{width:328px;height:206px;margin-top:16px}

.widgets{position:absolute;left:21px;top:1937px;width:1158px;height:425px;background:var(--panel);display:flex;padding:38px 18px 0 34px;gap:30px}
.widget{flex:1}
.widget h4{font-size:22px;margin-bottom:16px}
.entry{display:flex;gap:10px;padding-bottom:10px;margin-bottom:10px;border-bottom:1px solid var(--rule)}
.entry .thumb{flex:0 0 58px;height:56px}
.entry h5{font-family:"Yanone Kaffeesatz",sans-serif;font-weight:400;font-size:16px;color:var(--link);line-height:1.1}
.entry p{font-size:12.5px;line-height:1.4;color:var(--muted)}
.about-text{font-size:13px;line-height:1.45;color:var(--muted)}

.footer-bar{position:absolute;left:21px;top:2397px;width:1158px;height:65px;background:var(--panel);padding:12px 12px}
.copyright{position:absolute;left:12px;top:14px;font-size:14px;color:#444}
.footer-nav{position:absolute;left:572px;top:12px;width:520px;display:flex;flex-wrap:wrap;gap:4px 18px;list-style:none}
.footer-nav li{font-size:14.5px;color:var(--accent)}
</style>
</head>
<body>

<header>
  <div class="brand"><small>Chef</small>Reed Palmer</div>
  <h1 class="site-title">Our Pantry Remedy</h1>
  <p class="tagline">Better nutritional choices for positive healthy outcomes</p>
</header>

<ul class="main-nav">
  <li>About</li><li>Blog</li><li>Recipes</li><li>Health &amp; Wellness</li><li>Services</li><li>Confidentiality</li><li>Affordability</li><li>Blog</li><li>Articles</li><li>Friday Cocktails</li>
</ul>

<section class="hero">
  <div class="hero-photo" role="img" aria-label="Hands tearing fresh broccoli over a steel pot in a kitchen, with peppers on the counter"></div>
  <div class="hero-caption">
    <h2>LOREM IPSUM</h2>
    <p>Lorem Ipsum Dolor Sit Amet, Consectetur Adipiscing Elit. Nam Nec Rhoncus Risus. In Ultrices Lacinia Ipsum. In Ultrices Lacinia Ipsum. In Ultrices Lacinia Ipsum.</p>
  </div>
  <div class="pager"><span>1</span><span class="active">2</span><span>3</span></div>
</section>

<section class="intro">
  <div class="intro-col"><h3 class="heading">Welcome</h3><p>Lorem ipsum dolor sit amet, consectetur adipiscing elit. Nam nec rhoncus risus. In ultrices lacinia ipsum, posuere faucibus velit bibendum ac. Sed ultrices leo.</p></div>
  <div class="intro-col"><h3 class="heading">Who is Reed Palmer?</h3><p class="plain">My name is Reed Palmer and I grew up in Millbrook, Michigan. I graduated from Linden High School in 1974, Harbor State University in 1981 with a BA in Biology and then again in 1984 with a BS in Pharmacy.</p></div>
  <div class="intro-col"><h3 class="heading">Stay tuned</h3><p class="plain">Stay tuned as Reed Palmer trades Key West for New York City and culinary school. We're betting the only difference between the two cities is the height of the buildings.</p></div>
  <div class="intro-col"><h3 class="heading">More</h3><p>Lorem ipsum dolor sit amet, consectetur adipiscing elit. Nam nec rhoncus risus. In ultrices lacinia ipsum. In ultrices lacinia ipsum. In ultrices lacinia ipsum.</p></div>
</section>

<article class="post-card" style="left:21px;top:1069px">
  <h3 class="heading">Meet the mineral in the shadows: Magnesium</h3>
  <p class="tinted">Most likely you are not sitting around wondering or fretting about your....</p>
  <div class="post-photo" style="background:linear-gradient(135deg,#6fa43a,#c9473a 45%,#e2a63d 70%,#f2efe6)" role="img" aria-label="Fresh vegetables, fruit and green juices on a table"></div>
</article>
<article class="post-card" style="left:414px;top:1069px">
  <h3 class="heading">Rocking Our Island's Wellness Factor</h3>
  <p>I am so happy to be back in Key West and I....</p>
  <div class="post-photo" style="background:linear-gradient(160deg,#f1ede6,#d9c3a3 50%,#c7412f 80%,#8c6a45)" role="img" aria-label="Hands slicing mushrooms and tomatoes on a cutting board"></div>
</article>
<article class="post-card" style="left:810px;top:1069px">
  <h3 class="heading">The Bad Boys in Our Diet</h3>
  <p>After 8 months and a dozen columns, I am very happy to....</p>
  <div class="post-photo" style="background:linear-gradient(160deg,#8a1a2c,#d88a2a 45%,#e8b84a 60%,#3a2a22)" role="img" aria-label="A burger with french fries on a dark plate"></div>
</article>

<article class="post-card" style="left:21px;top:1494px">
  <h3 class="heading">Super Chia Seeds</h3>
  <p class="tinted">Good nutrition, wellness, healing, and longevity are common goals we all share....</p>
  <div class="post-photo" style="background:linear-gradient(135deg,#e9b133,#d4572a 50%,#9ec7c9 75%,#c63a2d)" role="img" aria-label="Bowls of vanilla chia seed pudding on a colourful tablecloth"></div>
</article>
<article class="post-card" style="left:414px;top:1494px">
  <h3 class="heading">FISH FOR DINNER</h3>
  <p>We are so lucky to have the ocean in our back yard....</p>
  <div class="post-photo" style="background:radial-gradient(circle at 50% 55%,#d99a55,#6f9a3a 45%,#f4f4f2 75%)" role="img" aria-label="Grilled fish fillet on green salad on a white plate"></div>
</article>
<article class="post-card" style="left:810px;top:1494px">
  <h3 class="heading">Hello world!</h3>
  <p>Welcome to SitePress. This is your first post. Edit or delete it,....</p>
  <div class="post-photo" style="background:radial-gradient(circle at 50% 50%,#e2b27a,#c9452f 40%,#5e8a34 60%,#f1f0ec 85%)" role="img" aria-label="Fish fillet with tomatoes and greens on a white plate"></div>
</article>

<section class="widgets">
  <div class="widget">
    <h4 class="heading">New from the blog</h4>
    <div class="entry"><div class="thumb" style="background:linear-gradient(135deg,#e2b27a,#5e8a34)" role="img" aria-label="Fish dish thumbnail"></div><div><h5>Hello world!</h5><p>Welcome to SitePress. This is your first post. Edit or delete it,...</p></div></div>
    <div class="entry"><div class="thumb" style="background:linear-gradient(135deg,#6fa43a,#c9473a)" role="img" aria-label="Vegetables thumbnail"></div><div><h5>Meet the mineral in the shadows: Magnesium</h5><p>Most likely you are not sitting around wondering or fretting about your...</p></div></div>
    <div class="entry"><div class="thumb" style="background:linear-gradient(135deg,#e9b133,#9ec7c9)" role="img" aria-label="Chia pudding thumbnail"></div><div><h5>Super Chia Seeds</h5><p>Good nutrition, wellness, healing, and longevity are common goals we all share....</p></div></div>
  </div>
  <div class="widget">
    <h4 class="heading">Popular Posts</h4>
    <div class="entry"><div class="thumb" style="background:linear-gradient(135deg,#d99a55,#6f9a3a)" role="img" aria-label="Fish dinner thumbnail"></div><div><h5>FISH FOR DINNER</h5><p>We are so lucky to have the ocean in our back yard....</p></div></div>
    <div class="entry"><div class="thumb" style="background:linear-gradient(135deg,#8a1a2c,#d88a2a)" role="img" aria-label="Burger thumbnail"></div><div><h5>The Bad Boys in Our Diet</h5><p>After 8 months and a dozen columns, I am very happy to...</p></div></div>
    <div class="entry"><div class="thumb" style="background:linear-gradient(135deg,#d9c3a3,#c7412f)" role="img" aria-label="Chopping vegetables thumbnail"></div><div><h5>Rocking Our Island's Wellness Factor</h5><p>I am so happy to be back in Key West and I...</p></div></div>
  </div>
  <div class="widget">
    <h4 class="heading">Popular Recipes</h4>
    <div class="entry"><div class="thumb" style="background:linear-gradient(135deg,#e9b133,#d4572a)" role="img" aria-label="Chia pudding thumbnail"></div><div><h5>Super Chia Seeds</h5><p>Good nutrition, wellness, healing, and longevity are common goals we all share....</p></div></div>
    <div class="entry"><div class="thumb" style="background:linear-gradient(135deg,#e2b27a,#5e8a34)" role="img" aria-label="Fish dish thumbnail"></div><div><h5>Hello world!</h5><p>Welcome to SitePress. This is your first post. Edit or delete it,...</p></div></div>
    <div class="entry"><div class="thumb" style="background:linear-gradient(135deg,#6fa43a,#c9473a)" role="img" aria-label="Vegetables thumbnail"></div><div><h5>Meet the mineral in the shadows: Magnesium</h5><p>Most likely you are not sitting around wondering or fretting about your...</p></div></div>
  </div>
  <div class="widget">
    <h4 class="heading">About</h4>
    <p class="about-text">My name is Reed Palmer and I grew up in Millbrook, Michigan. I graduated from Linden High School in 1974, Harbor State University in 1981 with a BA in Biology and then again in 1984 with a BS in Pharmacy. Lorem ipsum dolor sit amet, consectetur adipiscing elit. Nam nec rhoncus risus. In ultrices lacinia ipsum. In ultrices lacinia ipsum. In ultrices lacinia ipsum. Lorem ipsum dolor sit amet, consectetur adipiscing elit. Nam nec rhoncus risus. In ultrices lacinia ipsum. In ultrices lacinia ipsum. In ultrices lacinia ipsum. Contact: reed@example-demo.com</p>
  </div>
</section>

<footer class="footer-bar">
  <p class="copyright">All Rights Reserved 2014</p>
  <ul class="footer-nav">
    <li>About</li><li>Blog</li><li>Recipes</li><li>Health &amp; Wellness</li><li>Services</li><li>Confidentiality</li><li>Affordability</li><li>Blog</li><li>Articles</li><li>Friday Cocktails</li>
  </ul>
</footer>

</body>
</html>
```